Software Specialist in Artificial Intelligence innovation needs a smart and professional looking bus

Prefers a clean and professional design, yet portraying a class of its own and a world-class feel. We develop state-of-the-art software automation engines by deploying artificial intelligence that simulates the smartest brains that are able to simulate a human consultant and/or data scientist. Both single-sided or double-sided design is acceptable. Do not refer too much to our current website as we are also in the process of revamping it so that it better reflects who we are and what we do.
Updates

Project Deadline Extended
Reason: A substantial number of designs submitted to date deviates a fair bit from requirements and expectations. Feedbacks will be provided to all parties by today and as such, an extension is catered to accomodate re-submissions.

Target Market(s)

Software technology companies, software developers, enterprise clients that requires automation supported by Artificial Intelligence driven software solutions.

Industry/Entity Type

Software

Contact Information for Business Card

Marcus Tan
Chief Innovator
marcustan@veltrixia.com
mobile: +65 94567312
Company Name: Veltrixia Pte Ltd
Address: 14 Sorbank Road #05-11 Harlowe Point, Singapore 538422
Telephone: +65 63417250
Website: www.Veltrixia.com
Please do not include the titles of the above fields.

Font styles to use
Sans Serif
Other font styles liked:
• Calibri, Futura Condensed

Requirements
Must have
• Portrays a professional and innovative image. Should reflect that the company is into Artificial Intelligence software development, high tech kind of feel.
Nice to have
• A plus point would be if you can even come up with a new company logo for us, representing who we are. Our current company logo is attached.
Should not have
• Fanciful stuffs as it must portray a professional image. Prefers not to have the cloud "image" as part of the logo or in the name card.

```html
<!DOCTYPE html>
<html lang="en">
<head>
<meta charset="utf-8">
<title>Veltrixia Business Card</title>
<link href="https://fonts.googleapis.com/css2?family=Carlito:wght@400;700&display=swap" rel="stylesheet">
<style>
  :root {
    --backdrop: #efefef;
    --brand-red: #d13338;
    --ink: #231f20;
    --paper: #ffffff;
    --band: #231f20;
  }
  * { box-sizing: border-box; margin: 0; padding: 0; }
  html, body { width: 1200px; height: 900px; overflow: hidden; }
  body {
    background: var(--backdrop);
    font-family: "Carlito", Calibri, Arial, sans-serif;
    position: relative;
  }
  .card {
    position: absolute;
    top: 307px;
    width: 524px;
    height: 285px;
    overflow: hidden;
    box-shadow: 0 1px 4px rgba(0,0,0,0.25);
    background: var(--brand-red);
  }
  .card--front { left: 41px; }
  .card--back { left: 616px; }

  .wordmark {
    display: flex;
    justify-content: center;
    align-items: center;
    gap: 12px;
    font-weight: 700;
    letter-spacing: -0.5px;
    line-height: 1;
  }
  .wordmark__dot {
    flex: none;
    border-radius: 50%;
    background: var(--ink);
  }
  .tagline {
    text-align: center;
    color: var(--ink);
    line-height: 1;
  }

  .card--front .wordmark {
    position: absolute; left: 0; right: 0; top: 98px;
    font-size: 52px; color: var(--paper);
  }
  .card--front .wordmark__dot { width: 22px; height: 22px; }
  .card--front .tagline {
    position: absolute; left: 0; right: 0; top: 163px;
    font-size: 21px;
  }

  .back-header {
    position: absolute; left: 0; top: 0; width: 100%; height: 133px;
    background: var(--paper);
  }
  .back-header .wordmark {
    position: absolute; left: 0; right: 0; top: 29px;
    font-size: 44px; color: var(--brand-red);
  }
  .back-header .wordmark__dot { width: 18px; height: 18px; }
  .back-header .tagline {
    position: absolute; left: 0; right: 0; top: 85px;
    font-size: 18px; font-weight: 700;
  }
  .back-band {
    position: absolute; left: 0; top: 133px; width: 100%; height: 12px;
    background: var(--band);
  }
  .contact {
    position: absolute; left: 36px; top: 161px; right: 20px;
    color: var(--paper);
  }
  .contact__name {
    font-size: 19px; font-weight: 700; margin-bottom: 11px;
  }
  .contact__grid {
    display: grid;
    grid-template-columns: 244px 1fr;
    row-gap: 7px;
    font-size: 12px; font-weight: 700; line-height: 1.1;
  }
</style>
</head>
<body>
  <section class="card card--front">
    <div class="wordmark"><span class="wordmark__dot"></span>Veltrixia</div>
    <div class="tagline">Powering AI-driven Business Automation</div>
  </section>

  <section class="card card--back">
    <div class="back-header">
      <div class="wordmark"><span class="wordmark__dot"></span>Veltrixia</div>
      <div class="tagline">Powering AI-driven Business Automation</div>
    </div>
    <div class="back-band"></div>
    <div class="contact">
      <div class="contact__name">Marcus Tan Chief Innovator</div>
      <div class="contact__grid">
        <span>marcustan@veltrixia.com</span>
        <span>+65 63417250</span>
        <span>+65 94567312</span>
        <span>www.Veltrixia.com</span>
        <span>14 Sorbank Road #05-11<br>Harlowe Point, Singapore 538422</span>
        <span></span>
      </div>
    </div>
  </section>
</body>
</html>
```